Domestic violence resource cards for distribution to at-risk patients in an emergency department

Using the attached image(or very similar) and text document, a tri-fold business card is requested that integrates the image on the outside and the document content throughout the card's remaining faces. A creative format is requested, one that does not look like the typical cold, uncaring bullet point outlines that are found in similar resource projects. Bold or larger font sizes are requested for headings and body text is not required to be aligned or justified and the bullet points in the supplied document can be removed for creative license. Palattes should be clear, avoiding neons or implied target gender. Legibility is paramount, but again a creative presentation of a very serious subject is our goal. These cards are intended to be distributed to patients or others in the emergency department that may benefit from domestic violence resources. The business card size is mandatory so that the card can be concealed if needed by the receiver.
Updates

Reason: There are several revisions from designers that we are anxiously awaiting; we want to provide time for these designers to submit new designs but also continue spending time with their families and friends around the holiday season.

Target Market(s)

Patients and family in contact with emergency services

Industry/Entity Type

Healthcare

Contact Information for Business Card

Double sided tri-fold card with image on outer sides, text content and resource phone numbers on the exterior. When complete, the card should fold to standard US business card size.

Font styles to use
Other font styles liked:
• Designer's choice, but clear and legible

Requirements
Must have
• See above description. Card must be tri-fold, fold down to standard business card size, remain easily readable, and fold along the long edge.
Should not have
• Cartoon images; bloated fonts or clipart; bright, flashy neon or rainbow-like colors; additional graphics or charts.

```html
<!DOCTYPE html>
<html lang="en">
<head>
<meta charset="utf-8">
<title>Break the Silence – Resource Card</title>
<link href="https://fonts.googleapis.com/css2?family=Roboto+Condensed:ital,wght@0,400;0,700;1,400;1,700&family=Archivo+Black&display=swap" rel="stylesheet">
<style>
  :root {
    --bg: #d8c6a6;
    --card: #000000;
    --ink: #ffffff;
    --ink-soft: #e6e6e6;
    --bar: #ffffff;
    --bar-ink: #111111;
    --seam: #1c1c1c;
    --icon: #222222;
    --photo-dark: #1a1a1a;
    --photo-mid: #6d6d6d;
    --photo-light: #bdbdbd;
  }
  * { box-sizing: border-box; margin: 0; padding: 0; }
  html, body { width: 1200px; height: 837px; overflow: hidden; }
  body {
    background: var(--bg);
    font-family: "Roboto Condensed", "Arial Narrow", sans-serif;
    color: var(--ink);
    position: relative;
  }
  .strip {
    position: absolute;
    top: 44px;
    width: 450px;
    height: 744px;
    background: var(--card);
    display: flex;
    flex-direction: column;
  }
  .strip--outside { left: 124px; }
  .strip--inside { left: 636px; }
  .panel {
    position: relative;
    height: 248px;
    overflow: hidden;
  }
  .panel + .panel { border-top: 1px solid var(--seam); }

  .bullets { list-style: none; }
  .bullets li {
    position: relative;
    padding-left: 14px;
    font-size: 12px;
    line-height: 15px;
    margin-bottom: 3px;
  }
  .bullets li::before {
    content: "•";
    position: absolute;
    left: 2px;
  }

  /* Inside 4 */
  .panel--plan-more { padding: 10px 24px 0 24px; }

  /* Back */
  .panel--contacts {
    display: flex;
    flex-direction: column;
    align-items: center;
    justify-content: center;
    text-align: center;
  }
  .phone-icon {
    position: absolute;
    left: 44px;
    top: 62px;
    width: 80px;
    height: 80px;
  }
  .contacts { position: relative; font-size: 9px; line-height: 13.8px; }
  .contacts .name { font-style: italic; }
  .contacts .number { font-weight: 700; font-size: 9.5px; }
  .contacts .url { font-size: 12px; margin-top: 8px; display: block; }

  /* Front */
  .cover-photo {
    position: absolute;
    left: 40px;
    top: 18px;
    width: 220px;
    height: 220px;
    background: radial-gradient(ellipse at 45% 55%, var(--photo-light) 0%, var(--photo-mid) 40%, var(--photo-dark) 75%, var(--card) 100%);
  }
  .cover-title {
    position: absolute;
    left: 278px;
    top: 34px;
    font-family: "Archivo Black", "Arial Black", sans-serif;
    font-size: 33px;
    line-height: 41px;
  }
  .cover-title span { display: block; }
  .cover-title span:nth-child(2) { padding-left: 4px; }
  .cover-title span:nth-child(3) { padding-left: 9px; }
  .cover-url {
    position: absolute;
    left: 288px;
    top: 200px;
    font-size: 12.5px;
  }

  /* Inside headings */
  .heading-bar {
    background: var(--bar);
    color: var(--bar-ink);
    font-weight: 700;
    font-size: 17px;
    line-height: 22px;
    padding: 2px 26px;
    width: 396px;
  }
  .panel--signs .heading-bar { margin-top: 20px; }
  .panel--signs .bullets { padding: 10px 24px 0 30px; }
  .panel--signs .bullets li { margin-bottom: 0.6px; }
  .verdict {
    font-weight: 700;
    font-style: italic;
    font-size: 14px;
    padding: 6px 0 0 56px;
  }

  .panel--remember .heading-bar {
    margin: 26px 0 0 16px;
    font-style: italic;
    width: 394px;
  }
  .panel--remember .bullets {
    padding: 10px 0 0 40px;
    width: 320px;
    font-style: italic;
  }
  .panel--remember .bullets li { font-size: 12.5px; line-height: 18px; margin-bottom: 0; }
  .remember-photo {
    position: absolute;
    right: 18px;
    top: 62px;
    width: 118px;
    height: 180px;
    background: radial-gradient(ellipse at 55% 40%, var(--photo-light) 0%, var(--photo-mid) 35%, var(--photo-dark) 70%, var(--card) 100%);
  }

  .panel--leaving .heading-bar {
    margin-top: 20px;
    width: 394px;
    padding: 2px 24px;
    font-size: 16.5px;
  }
  .panel--leaving .bullets { padding: 18px 20px 0 30px; }
  .panel--leaving .bullets li { margin-bottom: 4px; }
</style>
</head>
<body>
  <section class="strip strip--outside" aria-label="Outside of card">
    <div class="panel panel--plan-more">
      <ul class="bullets">
        <li>Have a small bag packed and ready at a friend or relative’s house so you can leave quick</li>
        <li>Stay off social media or cancel you accounts so that you can’t be found online or through your friends</li>
        <li>Do not talk about your plans in public areas or in mixed groups</li>
        <li>Open a credit card or bank account in your name only and do not use it until you are ready</li>
        <li>Keep a chargedprepaid cell phone and a shelter hotline number ready for emergencies</li>
        <li>Review your plan often and only share with trusted friends or family</li>
        <li>Be careful: you are at most risk during the first 72 hours after leaving an abusive situation</li>
        <li>Seek help at a police station, firehouse or hospital if needed</li>
      </ul>
    </div>

    <div class="panel panel--contacts">
      <svg class="phone-icon" viewBox="0 0 24 24" aria-hidden="true">
        <path fill="var(--icon)" d="M6.6 10.8c1.4 2.8 3.8 5.1 6.6 6.6l2.2-2.2c.3-.3.7-.4 1-.2 1.1.4 2.3.6 3.6.6.6 0 1 .4 1 1V20c0 .6-.4 1-1 1C10.6 21 3 13.4 3 4c0-.6.4-1 1-1h3.5c.6 0 1 .4 1 1 0 1.3.2 2.5.6 3.6.1.3 0 .7-.2 1l-2.3 2.2z"/>
      </svg>
      <div class="contacts">
        <div class="name">Nationwide Safe Home Line</div>
        <div class="number">1-800-555-0142</div>
        <div class="name">Harbor House Metro: Domestic Violence Crisis Resource</div>
        <div class="number">303-555-0118</div>
        <div class="name">Crossroads Family Safety Resources</div>
        <div class="number">303-555-0163</div>
        <div class="name">The Support Point</div>
        <div class="number">1-888-555-0190</div>
        <div class="name">Oak Circle Violence Resources</div>
        <div class="number">303-555-0127</div>
        <div><span class="name">Quiet Bench: Sexual Assault Victim’s Advocate</span> <span class="number">303-555-0175</span></div>
        <div><span class="name">Kind Hearts Line: Teen Dating Resource</span> <span class="number">1-866-555-0136</span></div>
        <div class="name">or text “kind” to 55500</div>
        <span class="url">www.safeshelterfinder.org</span>
      </div>
    </div>

    <div class="panel panel--cover">
      <div class="cover-photo" role="img" aria-label="Black and white photograph of two clenched fists with wrists bound by rope"></div>
      <h1 class="cover-title"><span>Break</span><span>the</span><span>Silence</span></h1>
      <div class="cover-url">www.safeshelterfinder.org</div>
    </div>
  </section>

  <section class="strip strip--inside" aria-label="Inside of card">
    <div class="panel panel--signs">
      <h2 class="heading-bar">Does your partner ever…</h2>
      <ul class="bullets">
        <li>Hit, kick, push, choke or slap you?</li>
        <li>Intimidate you with weapons or harmful objects?</li>
        <li>Force you to engage in sexual acts?</li>
        <li>Threaten to hurt you, your children or your friends/family?</li>
        <li>Threaten to deport you or tell others your personal information?</li>
        <li>Control where you go, who you talk to or who you make friends with?</li>
        <li>Keep, hide or destroy your most important things?</li>
        <li>Blame, embarrass, or criticize you, make you feel worthless or guilty?</li>
        <li>Control your food, money, medicines or medical care?</li>
      </ul>
      <p class="verdict">You may be a victim of abuse or neglect!</p>
    </div>

    <div class="panel panel--remember">
      <h2 class="heading-bar">Always remember…</h2>
      <ul class="bullets">
        <li>You have a right to be safe anywhere</li>
        <li>You don’t deserve to be hit or threatened</li>
        <li>Your children deserve to grow up without violence</li>
        <li>You have a right to protect you or your children until you are out of danger</li>
        <li>You are not alone</li>
        <li>You have choices</li>
      </ul>
      <div class="remember-photo" role="img" aria-label="Black and white photograph of one hand tightly gripping another person's wrist"></div>
    </div>

    <div class="panel panel--leaving">
      <h2 class="heading-bar">Leaving can be tough and very dangerous.<br>Here are some tips to help you plan for safety:</h2>
      <ul class="bullets">
        <li>Know people you can talk to and ask them to call the police if they hear a disturbance coming from your home</li>
        <li>Teach your children how to contact the police or fire department</li>
        <li>Practice how to get you and your children out of your home quickly and safely</li>
        <li>Plan where you will go if you have to leave right away and know the location of local emergency shelters</li>
        <li>Leave copies of important papers, keys, cash, IDs, and medicine with a friend or relative you trust</li>
      </ul>
    </div>
  </section>
</body>
</html>
```